Simple, bright, clean website - 3 pages, easy to update with WordPress!

I want to update my website (brevatlo.com) with a brighter/cleaner interface. It is quite dark right now. I would like it to be similar to a partner site (https://www.velmo-482.com/). White with some orange highlights (matching the logo). I want to be able to easily update the site content. There should be 3 main pages: About, Services, Contact. I also like a design similar to tarnop.com

Target Market(s)

Anyone using technology to achieve business goals.

Industry/Entity Type

Managed Service Provider (IT)

Coding

Coded - Design and coding required

Number of Pages Required

3 page

Colors
F0912C
F2A743
F7CA91
FBE8D2
FDF5EE

Requirements
Must have
• Links to standard social media apps like LinkedIn, Facebook, etc.. Easy to edit and add pages.

```html
<!DOCTYPE html>
<html lang="en">
<head>
<meta charset="utf-8">
<title>Brevatlo Consulting</title>
<link href="https://fonts.googleapis.com/css2?family=Poppins:wght@400;500;600;700&display=swap" rel="stylesheet">
<style>
:root{
  --orange:#f5a418;
  --orange-deep:#f0912c;
  --cream:#fde8b4;
  --cream-soft:#fdebc4;
  --dark:#3a3a3a;
  --ink:#1c1c1c;
  --muted:#555;
  --white:#fff;
  --line:#8a8a8a;
}
*{box-sizing:border-box;margin:0;padding:0}
html,body{width:1200px;height:3225px;overflow:hidden}
body{position:relative;font-family:'Poppins',sans-serif;color:var(--ink);background:var(--white)}
.abs{position:absolute}
a{color:inherit;text-decoration:none}

.topbar{left:0;top:0;width:1200px;height:51px;background:var(--dark);color:#eee;font-size:16px;letter-spacing:.5px}
.topbar .item{position:absolute;top:14px;display:flex;align-items:center;gap:9px}
.topbar svg{fill:#eee}

.header{left:0;top:51px;width:1200px;height:84px;background:var(--white);box-shadow:0 3px 8px rgba(0,0,0,.12);z-index:3}
.brand{position:absolute;left:111px;top:16px;display:flex;align-items:center;gap:10px;font-size:40px;font-weight:400;color:#555;letter-spacing:1px}
.brand .dot{width:14px;height:14px;border-radius:50%;background:var(--orange)}
.nav{position:absolute;right:110px;top:30px;display:flex;gap:32px;font-size:17px;color:#333}

.hero{left:0;top:135px;width:1200px;height:615px;overflow:hidden}
.hero .photo{position:absolute;inset:0;background:linear-gradient(90deg,#f1f0ee 0%,#e9e7e3 35%,#b9b2a8 60%,#8a7f72 80%,#c9c4bc 100%)}
.hero .fade{position:absolute;inset:0;background:linear-gradient(90deg,rgba(255,255,255,.85) 0%,rgba(255,255,255,.55) 45%,rgba(255,255,255,0) 70%)}
.hero .wave{position:absolute;left:0;bottom:0}
.hero-copy{position:absolute;left:111px;top:150px;width:450px}
.hero-copy .kicker{font-size:30px;font-weight:400;color:#111}
.hero-copy h1{font-size:48px;font-weight:700;color:var(--orange);line-height:1.15;text-shadow:0 2px 3px rgba(0,0,0,.15)}
.hero-copy p{margin-top:22px;font-size:16px;line-height:27px;color:#222}

.section-title{position:absolute;left:0;width:1200px;text-align:center;font-size:40px;font-weight:600;color:var(--orange);letter-spacing:3px}

.card{top:919px;width:302px;height:294px;border:1.5px solid #666;border-radius:24px;text-align:center;background:var(--white)}
.card .ring{margin:24px auto 0;width:125px;height:125px;border-radius:50%;border:10px solid var(--orange);display:flex;align-items:center;justify-content:center}
.card h3{margin-top:20px;font-size:19px;font-weight:600;letter-spacing:1.2px}
.card h3 .chev{color:var(--orange)}
.card p{margin:10px auto 0;width:250px;font-size:15px;line-height:22px;color:#444;letter-spacing:.6px}

.btn{display:flex;align-items:center;justify-content:center;background:var(--orange);color:#111;font-size:16px;font-weight:500;letter-spacing:1.3px;border-radius:4px;box-shadow:0 3px 4px rgba(0,0,0,.2)}

.about{left:0;top:1386px;width:1200px;height:658px;background:linear-gradient(90deg,var(--cream-soft),var(--cream))}
.about h2{position:absolute;left:112px;top:78px;font-size:40px;font-weight:600;color:var(--orange);letter-spacing:3px}
.about .lead{position:absolute;left:112px;top:162px;width:620px;font-size:21px;font-weight:600;line-height:32px;letter-spacing:.5px}
.about .body{position:absolute;left:112px;top:276px;width:570px;font-size:15.5px;line-height:27.5px;letter-spacing:1px;text-align:justify;color:#333}
.about .dots{position:absolute;left:879px;top:104px}
.about .block{position:absolute;left:709px;top:425px;width:155px;height:148px;border-radius:24px;background:var(--orange)}
.about .photo{position:absolute;left:777px;top:144px;width:311px;height:378px;border-radius:20px;background:linear-gradient(135deg,#8b8a87,#4b4a48 45%,#2e2c2a 70%,#9a948b)}

.avatar{top:2215px;width:138px;height:138px;border-radius:50%;background:radial-gradient(circle at 50% 40%,#d7cfc6,#8a8580 70%,#3b3a3c)}
.quote{top:2382px;width:300px;text-align:center;font-size:16px;line-height:26px;letter-spacing:1px;color:#333}
.quote .mark{color:var(--orange);font-size:34px;font-weight:700;font-style:italic;position:absolute;left:10px;top:-14px}
.quote .who{display:block;margin-top:8px;font-size:21px;font-weight:600;letter-spacing:1.5px;color:#111}
.pager{left:546px;top:2537px;display:flex;gap:9px}
.pager span{width:19px;height:19px;border-radius:50%;background:#c9c9c9}
.pager span.on{background:var(--orange)}

.footer{left:0;top:2791px;width:1200px;height:434px;background:radial-gradient(ellipse at 80% 40%,#4a4a4a,#383838 60%,#333)}
.cta{left:112px;top:2662px;width:978px;height:258px;border-radius:62px;background:var(--cream-soft);text-align:center;z-index:2}
.cta p{margin-top:66px;font-size:27px;font-weight:500;line-height:36px;letter-spacing:2.5px;color:#111}
.cta .btn{position:absolute;left:238px;top:150px;width:503px;height:42px;font-size:16px}
.foot-brand{left:0;width:1200px;top:2990px;display:flex;justify-content:center;align-items:center;gap:10px;font-size:48px;color:#f2f2f2;letter-spacing:1px}
.foot-brand .dot{width:14px;height:14px;border-radius:50%;background:var(--orange)}
.foot-nav{left:0;width:1200px;top:3060px;display:flex;justify-content:center;gap:40px;font-size:21px;font-weight:500;color:#f2f2f2}
.social{left:537px;top:3106px;display:flex;gap:5px}
.social span{width:22px;height:22px;border:1.5px solid #eee;border-radius:50%}
.rule{left:112px;top:3161px;width:978px;height:1px;background:var(--line)}
.legal{left:112px;top:3182px;width:978px;display:flex;justify-content:space-between;font-size:15px;font-weight:500;color:#f2f2f2}
</style>
</head>
<body>

<div class="abs topbar">
  <div class="item" style="left:111px">
    <svg width="15" height="12" viewBox="0 0 15 12"><path d="M0 0h15v12H0z M1 1.5l6.5 5 6.5-5" fill="#eee"/><path d="M1 1.5l6.5 5 6.5-5" stroke="#3a3a3a" stroke-width="1.4" fill="none"/></svg>
    info@brevatlo.com
  </div>
  <div class="item" style="left:325px">
    <svg width="15" height="15" viewBox="0 0 24 24"><path d="M6.6 10.8a15 15 0 0 0 6.6 6.6l2.2-2.2c.3-.3.7-.4 1-.2 1.1.4 2.3.6 3.6.6.6 0 1 .4 1 1V20c0 .6-.4 1-1 1A17 17 0 0 1 3 4c0-.6.4-1 1-1h3.5c.6 0 1 .4 1 1 0 1.3.2 2.5.6 3.6.1.3 0 .7-.2 1z"/></svg>
    +1 888 8888 8888
  </div>
  <div class="item" style="right:110px">
    <svg width="12" height="16" viewBox="0 0 12 16"><path d="M6 0a6 6 0 0 0-6 6c0 4.5 6 10 6 10s6-5.5 6-10a6 6 0 0 0-6-6z"/></svg>
    Sed ut perspiciatis unde
  </div>
</div>

<header class="abs header">
  <a class="brand" href="#"><span>brevatlo</span><span class="dot"></span></a>
  <nav class="nav"><a href="#">About Us</a><a href="#">Services</a><a href="#">Contact Us</a></nav>
</header>

<section class="abs hero">
  <div class="photo" role="img" aria-label="Business team meeting around a table in a bright office"></div>
  <div class="fade"></div>
  <svg class="wave" width="1200" height="140" viewBox="0 0 1200 140" preserveAspectRatio="none">
    <path d="M0 95 C200 20 420 45 640 60 C860 75 1020 90 1200 40 L1200 140 L0 140 Z" fill="#fff"/>
  </svg>
  <div class="hero-copy">
    <div class="kicker">Welcome To</div>
    <h1>Brevatlo Consulting</h1>
    <p>Lorem ipsum dolor sit amet, consectetur adipiscing elit, sed do eiusmod tempor incididunt ut labore et dolore magna aliqua.</p>
  </div>
</section>

<h2 class="section-title" style="top:830px">Our Services</h2>

<article class="abs card" style="left:112px">
  <div class="ring"><svg width="52" height="52" viewBox="0 0 52 52" fill="none" stroke="#333" stroke-width="2.2"><rect x="6" y="12" width="40" height="28" rx="2"/><path d="M2 44h48"/><path d="M18 20h16M26 20v14"/></svg></div>
  <h3>Managed IT Services <span class="chev">›</span></h3>
  <p>Lorem ipsum dolor sit amet, consectetur adipiscing elit, sed do eiusmod</p>
</article>
<article class="abs card" style="left:450px">
  <div class="ring"><svg width="52" height="52" viewBox="0 0 52 52" fill="none" stroke="#333" stroke-width="2.2"><rect x="4" y="12" width="40" height="28" rx="2"/><path d="M18 46h12M24 40v6"/><circle cx="36" cy="14" r="7"/><circle cx="36" cy="14" r="2.5"/></svg></div>
  <h3>IT Consulting <span>›</span></h3>
  <p>Lorem ipsum dolor sit amet, consectetur adipiscing elit, sed do eiusmod</p>
</article>
<article class="abs card" style="left:788px">
  <div class="ring"><svg width="52" height="52" viewBox="0 0 52 52" fill="none" stroke="#333" stroke-width="2.2"><path d="M14 30a9 9 0 0 1 2-18 12 12 0 0 1 22 2 8 8 0 0 1 0 16z"/><rect x="10" y="28" width="22" height="16" rx="2"/><circle cx="36" cy="30" r="5"/></svg></div>
  <h3>Cloud Services <span>›</span></h3>
  <p>Lorem ipsum dolor sit amet, consectetur adipiscing elit, sed do eiusmod</p>
</article>

<a class="abs btn" href="#" style="left:513px;top:1260px;width:174px;height:41px">View More</a>

<section class="abs about">
  <h2>About - Brevatlo Consulting</h2>
  <p class="lead">Lorem ipsum dolor sit amet, consectetur adipiscing elit, sed do eiusmod tempor incididunt ut labore et dolore magna aliqua.</p>
  <p class="body">Lorem ipsum dolor sit amet, consectetur adipiscing elit, sed do eiusmod tempor incididunt ut labore et dolore magna aliqua. Quis ipsum suspendisse ultrices gravida. Risus commodo viverra maecenas accumsan lacus vel facilisis. Lorem ipsum dolor sit amet, consectetur adipiscing elit, sed do eiusmod tempor incididunt ut labore et dolore magna aliqua. Quis ipsum suspendisse ultrices gravida.</p>
  <a class="btn" href="#" style="position:absolute;left:112px;top:480px;width:175px;height:42px">Learn More</a>
  <svg class="dots" width="262" height="86" viewBox="0 0 262 86" fill="#cfc3a8">
    <g>
      <circle cx="5" cy="5" r="4.5"/><circle cx="30" cy="5" r="4.5"/><circle cx="55" cy="5" r="4.5"/><circle cx="80" cy="5" r="4.5"/><circle cx="105" cy="5" r="4.5"/><circle cx="130" cy="5" r="4.5"/><circle cx="155" cy="5" r="4.5"/><circle cx="180" cy="5" r="4.5"/><circle cx="205" cy="5" r="4.5"/><circle cx="230" cy="5" r="4.5"/><circle cx="255" cy="5" r="4.5"/>
      <circle cx="5" cy="25" r="4.5"/><circle cx="30" cy="25" r="4.5"/><circle cx="55" cy="25" r="4.5"/><circle cx="80" cy="25" r="4.5"/><circle cx="105" cy="25" r="4.5"/><circle cx="130" cy="25" r="4.5"/><circle cx="155" cy="25" r="4.5"/><circle cx="180" cy="25" r="4.5"/><circle cx="205" cy="25" r="4.5"/><circle cx="230" cy="25" r="4.5"/><circle cx="255" cy="25" r="4.5"/>
      <circle cx="205" cy="45" r="4.5"/><circle cx="230" cy="45" r="4.5"/><circle cx="255" cy="45" r="4.5"/>
      <circle cx="230" cy="65" r="4.5"/><circle cx="255" cy="65" r="4.5"/>
      <circle cx="230" cy="82" r="4"/><circle cx="255" cy="82" r="4"/>
    </g>
  </svg>
  <div class="block"></div>
  <div class="photo" role="img" aria-label="Two colleagues in discussion at an office table with a laptop"></div>
</section>

<h2 class="section-title" style="top:2120px">Testimonials</h2>

<div class="abs avatar" style="left:205px" role="img" aria-label="Client portrait"></div>
<div class="abs avatar" style="left:531px" role="img" aria-label="Client portrait"></div>
<div class="abs avatar" style="left:858px" role="img" aria-label="Client portrait"></div>

<blockquote class="abs quote" style="left:124px"><span class="mark">"</span>Lorem ipsum dolor sit amet, consectetur adipiscing elit, sed do eiusmod tempor<span class="who">- John Peter</span></blockquote>
<blockquote class="abs quote" style="left:450px"><span class="mark">"</span>Lorem ipsum dolor sit amet, consectetur adipiscing elit, sed do eiusmod tempor<span class="who">- John Peter</span></blockquote>
<blockquote class="abs quote" style="left:777px"><span class="mark">"</span>Lorem ipsum dolor sit amet, consectetur adipiscing elit, sed do eiusmod tempor<span class="who">- John Peter</span></blockquote>

<div class="abs pager"><span></span><span></span><span class="on"></span><span></span></div>

<footer class="abs footer"></footer>

<div class="abs cta">
  <p>Sign up with Brevatlo and enjoy the benefits of a<br>long-term business relationship</p>
  <a class="btn" href="#">Sign Up With Free Cybersecurity Assessment</a>
</div>

<div class="abs foot-brand"><span>brevatlo</span><span class="dot"></span></div>
<nav class="abs foot-nav"><a href="#">About Us</a><a href="#">Services</a><a href="#">Contact Us</a></nav>
<div class="abs social" aria-label="Social media links"><span></span><span></span><span></span><span></span><span></span></div>
<div class="abs rule"></div>
<div class="abs legal">
  <span>©2024 Brevatlo Consulting inc All Rights Reserved.</span>
  <span>Privacy Policy &nbsp;|&nbsp; Sitemap</span>
</div>

</body>
</html>
```